Dental Magazine Cover

I need a template created for a magazine cover. Magazine title is "Dentistry Halvern"

I would like to have a logo designed for "Dentistry Halvern"

For each issue, we would like to keep the same basic template and change out the photos, text, etc. according to the contents of the issue.

You can create the cover of the first issue with the attached photos and captions:

Date for use on magazine cover is February 2014

Main caption: Maxillary Reconstruction with Immediately Loaded Dental Implants
(Use attached File 1 for main photo. Photo may be cropped and rotated as needed)

Inset: Bisphosphonate Guidelines for Dental Treatment
(Use attached file 2 for inset photo. Photo may be cropped and rotated as needed).

Target Market(s)

Target audience for this magazine are dentists, dental hygienists, dental assistants, and dental professionals in the Austin, Texas area.

Industry/Entity Type

Dental

Other font styles liked:
• Font need to "POP"

Requirements
Must have
• Please see project overview guidelines. Magazine cover needs to have the following:
1) Logo
2) Main image
3) Caption for Main image (Maxillary Reconstruction with Immediately Loaded Dental Implants)
4) Smaller Inset Photo
5) Caption for smaller inset photo (Bisphosphonate Guidelines for Dental Treatment)
6) Date of magazine issue (February 2014)

Use any of the Photos you see fit to make the magazine cover work.
Nice to have
• Please try to make the "Dentistry Halvern" logo "POP". Dental journals are boring enough. We can at least have a logo that pops. Simply using generic text will win this design. The below text is just a suggestion of a Logo. Please feel free to use all creative license in making a logo that has some sizzle. PLEASE NOTE: A tooth is NOT needed in the logo...

```html
<!DOCTYPE html>
<html lang="en">
<head>
<meta charset="utf-8">
<title>Dentistry Halvern – February 2014</title>
<link rel="stylesheet" href="https://fonts.googleapis.com/css2?family=Arimo:wght@400;700&display=swap">
<style>
  :root {
    --cover-mint: #cbe2d6;
    --masthead-blue: #1f3d9c;
    --panel-black: #000000;
    --caption-white: #ffffff;
    --accent-yellow: #f5d90a;
    --ink: #111111;
    --frame-white: #ffffff;
  }
  * { margin: 0; padding: 0; box-sizing: border-box; }
  html, body {
    width: 935px;
    height: 1200px;
    overflow: hidden;
    background: var(--cover-mint);
  }
  .cover {
    position: relative;
    width: 935px;
    height: 1200px;
    background: var(--cover-mint);
    font-family: "Arimo", Arial, sans-serif;
    color: var(--ink);
  }
  .masthead {
    position: absolute;
    left: 34px;
    top: 52px;
    font-weight: 700;
    font-size: 71px;
    letter-spacing: 1px;
    line-height: 1;
    color: var(--masthead-blue);
    text-transform: uppercase;
    white-space: nowrap;
  }
  .issue-date {
    position: absolute;
    left: 35px;
    top: 228px;
    font-size: 21px;
    font-weight: 400;
  }
  .issue-date strong { font-weight: 700; }
  .feature-panel {
    position: absolute;
    left: 33px;
    top: 293px;
    width: 872px;
    height: 757px;
    background: var(--panel-black);
    border-top-right-radius: 46px;
    overflow: hidden;
  }
  .feature-photo {
    position: absolute;
    left: 95px;
    top: 110px;
    width: 690px;
    height: 380px;
    background: radial-gradient(ellipse at 50% 50%,
      #f1eee4 0%, #d9b3a3 28%, #b98a72 48%, #5a4136 68%, rgba(0,0,0,0) 80%);
  }
  .feature-caption {
    position: absolute;
    right: 50px;
    top: 475px;
    text-align: right;
    color: var(--caption-white);
    text-transform: uppercase;
    line-height: 1.2;
  }
  .feature-caption .line-large { font-size: 36px; display: block; }
  .feature-caption .line-small { font-size: 24px; display: block; margin-top: 4px; }
  .feature-caption .line-accent {
    font-size: 43px;
    font-weight: 700;
    color: var(--accent-yellow);
    display: block;
    margin-top: 2px;
  }
  .inset-photo {
    position: absolute;
    left: 67px;
    top: 1003px;
    width: 246px;
    height: 168px;
    border: 4px solid var(--frame-white);
    border-radius: 14px;
    background: linear-gradient(135deg,
      #3b7fd0 0%, #d9d2c4 30%, #c64aa8 50%, #e8d46a 70%, #3bb6a0 100%);
  }
  .inset-caption {
    position: absolute;
    left: 348px;
    top: 1073px;
    font-size: 21px;
    line-height: 1.3;
    text-transform: uppercase;
  }
  .inset-caption strong { font-weight: 700; display: block; }
  .inset-caption span { display: block; }
</style>
</head>
<body>
  <main class="cover">
    <h1 class="masthead">Dentistry Halvern</h1>
    <p class="issue-date">February <strong>2014</strong></p>

    <section class="feature-panel">
      <div class="feature-photo" role="img" aria-label="Full-arch upper implant prosthesis on a plaster model, lit against a black background"></div>
      <h2 class="feature-caption">
        <span class="line-large">Maxillary</span>
        <span class="line-large">Reconstruction</span>
        <span class="line-small">With Immediately Loaded</span>
        <span class="line-accent">Dental Implants</span>
      </h2>
    </section>

    <div class="inset-photo" role="img" aria-label="Colourful micro-scan of trabecular bone structure"></div>
    <p class="inset-caption">
      <strong>Bisphosphonate</strong>
      <strong>Guidelines</strong>
      <span>For Dental Treatment</span>
    </p>
  </main>
</body>
</html>
```